P.K.Harbor Services Business Card

We need a bi-lingual card (spanish/english). Information should be name, hours, services and address/phone. I am including a flyer as a reference--much of the information is included on it (spanish/english as well). THE COMPANY IS CALLED "P.K. HARBOR SERVICES" AND WE THINK THAT "P.K." SHOULD SUFFICE AS A LOGO--BUT WE DON'T HAVE THAT FONT NAILED DOWN. Colors should be Green/Blue scale. Happy colors. It's a check cashing business.

```html
<!DOCTYPE html>
<html lang="en">
<head>
<meta charset="utf-8">
<title>P.K. Harbor Services – Business Card</title>
<link href="https://fonts.googleapis.com/css2?family=Montserrat:wght@600;800&family=Arimo:wght@400&family=Oswald:wght@500;600&family=Playball&display=swap" rel="stylesheet">
<style>
  :root{
    --bg:#3a3a3c;
    --blue:#4398dc;
    --blue-dark:#2f74b3;
    --teal:#5aa0a0;
    --green:#8bb13a;
    --white:#ffffff;
    --ink:#1d1d1d;
    --grey:#4a4a4a;
  }
  *{box-sizing:border-box;margin:0;padding:0}
  html,body{width:1200px;height:1015px;overflow:hidden;background:var(--bg)}
  .canvas{position:relative;width:1200px;height:1015px}
  .card{position:absolute;left:220px;width:760px;height:434px;overflow:hidden;box-shadow:0 14px 30px rgba(0,0,0,.45)}
  .card-front{top:40px;background:linear-gradient(180deg,var(--blue) 0%,var(--teal) 40%,var(--green) 100%)}
  .card-back{top:534px;background:var(--white)}

  .brand{position:absolute;font-family:"Montserrat",sans-serif;text-align:center}
  .brand-mark{display:flex;align-items:center;justify-content:center;gap:16px}
  .brand-square{width:22px;height:22px}
  .brand-initials{font-weight:800;line-height:1}
  .brand-name{font-weight:600;letter-spacing:.08em}

  .card-front .brand{left:0;right:0;top:130px;color:var(--white)}
  .card-front .brand-square{background:var(--white)}
  .card-front .brand-initials{font-size:120px}
  .card-front .brand-name{font-size:30px;margin-top:10px}

  .card-back .brand{left:40px;top:38px;color:var(--green);text-align:left}
  .card-back .brand-mark{justify-content:flex-start;gap:12px}
  .card-back .brand-square{background:var(--blue);width:16px;height:16px}
  .card-back .brand-initials{font-size:76px}
  .card-back .brand-name{font-size:19px;color:var(--grey);margin-top:6px}

  .back-art{position:absolute;inset:0}

  .contact{position:absolute;right:36px;top:28px;text-align:right;font-family:"Arimo",sans-serif;color:var(--ink);line-height:1.2}
  .contact-phone{font-size:30px}
  .contact-hours{font-size:16px}
  .contact-address{font-size:19px;margin-top:10px}

  .partners{position:absolute;right:30px;top:185px;width:330px;display:flex;flex-wrap:wrap;justify-content:flex-end;gap:10px 18px;font-family:"Arimo",sans-serif;font-size:15px;color:var(--ink)}
  .partner{display:flex;align-items:center;gap:6px}
  .partner-dot{width:14px;height:14px;border-radius:50%;background:var(--ink)}

  .offer{position:absolute;left:40px;top:296px;color:var(--white)}
  .offer-title{font-family:"Oswald",sans-serif;font-weight:600;font-size:38px;line-height:1}
  .offer-subtitle{font-family:"Oswald",sans-serif;font-weight:500;font-size:17px;letter-spacing:.06em;line-height:1.3;margin-bottom:2px}
  .offer-line{font-family:"Playball",cursive;font-size:22px;line-height:1.2}
</style>
</head>
<body>
<main class="canvas">
  <section class="card card-front">
    <div class="brand">
      <div class="brand-mark"><span class="brand-square"></span><span class="brand-initials">P.K.</span></div>
      <div class="brand-name">HARBOR SERVICES</div>
    </div>
  </section>

  <section class="card card-back">
    <svg class="back-art" viewBox="0 0 760 434" preserveAspectRatio="none" aria-hidden="true">
      <polygon points="0,290 440,262 610,434 0,434" fill="var(--green)"/>
      <polygon points="440,222 760,360 760,400 700,434 660,434 440,272" fill="var(--blue)"/>
      <polygon points="390,248 440,222 440,272 390,300" fill="var(--blue-dark)"/>
    </svg>

    <div class="brand">
      <div class="brand-mark"><span class="brand-initials">P.K.</span><span class="brand-square"></span></div>
      <div class="brand-name">HARBOR SERVICES</div>
    </div>

    <div class="contact">
      <div class="contact-phone">(914) 555 - 0182</div>
      <div class="contact-hours">MONDAY-SATURDAY (9AM-9PM)</div>
      <div class="contact-hours">LUNES-SÁBADO (9AM-9PM)</div>
      <div class="contact-address">48 BIRCH LANE<br>MAPLE RIDGE, NY</div>
    </div>

    <div class="partners">
      <span class="partner"><span class="partner-dot"></span>NovaCard</span>
      <span class="partner">State Lotto</span>
      <span class="partner">Tempo Minutes</span>
      <span class="partner">BillEase Pay</span>
      <span class="partner">Globe Transfer</span>
    </div>

    <div class="offer">
      <div class="offer-title">CHECK CA$HING</div>
      <div class="offer-subtitle">CAMBIO DE CHEQUES</div>
      <div class="offer-line">All Checks Welcome! · ¡Todos los Cheques!</div>
      <div class="offer-line">Best Rates · Las Mejores Tarifas</div>
    </div>
  </section>
</main>
</body>
</html>
```